Business Card Revision

Need to redesign my business cards for a new professional look. We are a courier company. You can go to www.qvroutefast.com to see what we do. The trucks have an old company name (Nimble) on them but that is the company we are just now
changing the name.

Target Market(s)

Potential clients. We service the automotive, plumbing, printing, air freight industries as well as many others.

Industry/Entity Type

Business

Contact Information for Business Card

QVrushline
20583 Palmer Fenwick Parkway
Cincinnati, Oh 45317

Howard T. Lassiter
President

howie@qvroutefast.com

Main: (513) 555-0147

```html
<!DOCTYPE html>
<html lang="en">
<head>
<meta charset="utf-8">
<title>QVrushline Business Card</title>
<link rel="stylesheet" href="https://fonts.googleapis.com/css2?family=Open+Sans:wght@400;600;800&display=swap">
<style>
  :root {
    --page: #e9e6e1;
    --card-black: #0b0b0c;
    --brand-green: #3fb94f;
    --band-green: #45bd55;
    --brand-blue: #2d8fd0;
    --ink-light: #f4fbf5;
  }
  html, body {
    margin: 0;
    width: 1200px;
    height: 1022px;
    overflow: hidden;
    background: var(--page);
    font-family: "Open Sans", Arial, sans-serif;
  }
  .card {
    position: absolute;
    left: 100px;
    top: 225px;
    width: 1000px;
    height: 571px;
    background: var(--card-black);
    overflow: hidden;
    box-shadow: 0 18px 40px rgba(0,0,0,.25);
  }
  .contact-band {
    position: absolute;
    inset: 0;
    width: 100%;
    height: 100%;
  }
  .company-name {
    position: absolute;
    left: 56px;
    top: 40px;
    margin: 0;
    font-weight: 800;
    font-size: 118px;
    letter-spacing: 4px;
    line-height: 1;
    color: var(--brand-green);
    text-transform: uppercase;
  }
  .person {
    position: absolute;
    left: 60px;
    top: 250px;
  }
  .person-name {
    margin: 0;
    font-weight: 600;
    font-size: 34px;
    color: var(--brand-blue);
  }
  .person-title {
    margin: 2px 0 0;
    font-size: 22px;
    color: var(--brand-green);
  }
  .contact-list {
    position: absolute;
    left: 500px;
    top: 330px;
    margin: 0;
    padding: 0;
    list-style: none;
    color: var(--ink-light);
    font-size: 24px;
    line-height: 40px;
  }
  .contact-list li { display: flex; align-items: center; }
  .contact-list .plain { padding-left: 0; }
  .contact-icon {
    width: 18px;
    height: 18px;
    margin-right: 12px;
    flex: none;
  }
</style>
</head>
<body>
  <main class="card">
    <svg class="contact-band" viewBox="0 0 1000 571" aria-hidden="true">
      <polygon points="460,300 760,300 760,150 1000,150 1000,571 460,571" fill="var(--band-green)"/>
    </svg>

    <h1 class="company-name">QVrushline</h1>

    <div class="person">
      <p class="person-name">Howard T. Lassiter</p>
      <p class="person-title">President</p>
    </div>

    <ul class="contact-list">
      <li class="plain">20583 Palmer Fenwick Parkway</li>
      <li class="plain">Cincinnati, Oh 45317</li>
      <li>
        <svg class="contact-icon" viewBox="0 0 24 24" aria-hidden="true"><path fill="#fff" d="M6.6 10.8a15.1 15.1 0 0 0 6.6 6.6l2.2-2.2c.3-.3.7-.4 1-.2 1.1.4 2.3.6 3.6.6.6 0 1 .4 1 1V20c0 .6-.4 1-1 1A17 17 0 0 1 3 4c0-.6.4-1 1-1h3.5c.6 0 1 .4 1 1 0 1.3.2 2.5.6 3.6.1.3 0 .7-.2 1z"/></svg>
        (513) 555-0147
      </li>
      <li>
        <svg class="contact-icon" viewBox="0 0 24 24" aria-hidden="true"><rect x="2" y="5" width="20" height="14" rx="2" fill="none" stroke="#fff" stroke-width="2"/><path d="M3 6l9 7 9-7" fill="none" stroke="#fff" stroke-width="2"/></svg>
        howie@qvroutefast.com
      </li>
      <li>
        <svg class="contact-icon" viewBox="0 0 24 24" aria-hidden="true"><circle cx="12" cy="12" r="9" fill="none" stroke="#fff" stroke-width="2"/><path d="M3 12h18M12 3c3 3 3 15 0 18M12 3c-3 3-3 15 0 18" fill="none" stroke="#fff" stroke-width="1.6"/></svg>
        www.qvroutefast.com
      </li>
    </ul>
  </main>
</body>
</html>
```